Real Estate Investing company needs a business card design

We need a business card design for new Real Estate Investment Company called "Maple Ridge Ventures, LLC." We buy homes for cash and close quickly in any situation. Our company provides an easy and fast option for home owners who are in tough situations who need to sell their home fast and don't want realtor fees or other listing hassles. We also renovate and resell our homes which helps provide housing for the community. We would like to see designs that use the colors blue and white to match our company logo or other colors that may match our company logo. The final design should communicate trust and easy process.
Industry/Entity Type
Business
Contact Information for Business Card
Front should have company name and company logo. back of card should have company logo and area to list services.
Look and feel

```html
<!DOCTYPE html>
<html lang="en">
<head>
<meta charset="utf-8">
<title>Maple Ridge Ventures – Business Cards</title>
<link href="https://fonts.googleapis.com/css2?family=Open+Sans:wght@400;600;700&display=swap" rel="stylesheet">
<style>
  :root {
    --brand-blue: #0d63b8;
    --brand-blue-light: #1676c9;
    --brand-blue-dark: #0a4e98;
    --card-white: #ffffff;
    --backdrop: #5a4a52;
    --ink-light: #ffffff;
  }
  * { box-sizing: border-box; margin: 0; padding: 0; }
  html, body { width: 1200px; height: 800px; overflow: hidden; }
  body {
    background: var(--backdrop);
    font-family: "Open Sans", Arial, sans-serif;
    display: flex;
    align-items: center;
    justify-content: center;
    gap: 48px;
  }
  .card {
    position: relative;
    width: 540px;
    height: 309px;
    background: var(--card-white);
    overflow: hidden;
    box-shadow: 0 10px 30px rgba(0,0,0,0.35);
  }
  .brand-name {
    display: flex;
    align-items: center;
    gap: 12px;
    color: var(--brand-blue);
    font-weight: 700;
    white-space: nowrap;
  }
  .brand-mark {
    width: 18px;
    height: 18px;
    background: var(--brand-blue);
    flex: none;
  }

  /* Contact side */
  .card-contact .top-strip {
    position: absolute; top: 0; right: 0;
    width: 330px; height: 14px;
    background: var(--brand-blue-light);
  }
  .card-contact .brand-name {
    position: absolute; top: 68px; left: 150px;
    font-size: 26px;
  }
  .contact-band {
    position: absolute; left: 0; bottom: 0;
    width: 100%; height: 150px;
    background: var(--brand-blue);
    display: flex;
  }
  .person {
    width: 218px;
    padding: 40px 0 0 26px;
    color: var(--ink-light);
  }
  .person-name {
    font-size: 22px; font-weight: 400; letter-spacing: 0.5px;
    padding: 0 0 4px 44px;
    border-top: 1.5px solid var(--ink-light);
    padding-top: 4px;
    width: 150px;
  }
  .person-role {
    font-size: 19px; font-weight: 400;
    padding: 4px 0 6px 10px;
    border-bottom: 1.5px solid var(--ink-light);
    width: 150px;
  }
  .icon-column {
    width: 44px;
    background: var(--brand-blue-dark);
    display: flex; flex-direction: column;
    align-items: center; justify-content: center;
    gap: 12px;
    border-right: 3px solid var(--ink-light);
  }
  .icon-column svg { width: 16px; height: 16px; }
  .contact-list {
    list-style: none;
    display: flex; flex-direction: column; justify-content: center;
    gap: 6px;
    padding-left: 16px;
    color: var(--ink-light);
    font-size: 14px;
  }

  /* Logo side */
  .card-front .top-strip {
    position: absolute; top: 0; right: 0;
    width: 300px; height: 22px;
    background: var(--brand-blue-light);
  }
  .card-front .bottom-strip {
    position: absolute; bottom: 0; left: 0;
    width: 330px; height: 22px;
    background: var(--brand-blue);
  }
  .card-front .brand-name {
    position: absolute; top: 50%; left: 50%;
    transform: translate(-50%, -50%);
    font-size: 34px;
  }
</style>
</head>
<body>

  <section class="card card-contact" aria-label="Business card, contact side">
    <div class="top-strip"></div>
    <div class="brand-name"><span class="brand-mark"></span>Maple Ridge Ventures</div>
    <div class="contact-band">
      <div class="person">
        <p class="person-name">NAME</p>
        <p class="person-role">POSITION</p>
      </div>
      <div class="icon-column">
        <svg viewBox="0 0 16 16" aria-label="phone"><circle cx="8" cy="8" r="8" fill="#fff"/><path d="M5 4.5h2l.6 2-1 .8a5 5 0 0 0 2.1 2.1l.8-1 2 .6v2c-3.5.3-6.8-3-6.5-6.5z" fill="#0a4e98"/></svg>
        <svg viewBox="0 0 16 16" aria-label="email"><circle cx="8" cy="8" r="8" fill="#fff"/><rect x="4" y="5.5" width="8" height="5.5" fill="none" stroke="#0a4e98" stroke-width="1"/><path d="M4 5.5l4 3 4-3" fill="none" stroke="#0a4e98" stroke-width="1"/></svg>
        <svg viewBox="0 0 16 16" aria-label="address"><circle cx="8" cy="8" r="8" fill="#fff"/><path d="M8 12.5s-3-3.2-3-5.3a3 3 0 0 1 6 0c0 2.1-3 5.3-3 5.3z" fill="#0a4e98"/><circle cx="8" cy="7.2" r="1" fill="#fff"/></svg>
        <svg viewBox="0 0 16 16" aria-label="website"><circle cx="8" cy="8" r="8" fill="#fff"/><g fill="none" stroke="#0a4e98" stroke-width="0.9"><circle cx="8" cy="8" r="4"/><ellipse cx="8" cy="8" rx="1.8" ry="4"/><path d="M4 8h8"/></g></svg>
      </div>
      <ul class="contact-list">
        <li>+1 555 014 2290</li>
        <li>hello@mapleridgeventures.com</li>
        <li>48 Alder Lane, Brookfield, Oregon</li>
        <li>www.mapleridgeventures.com</li>
      </ul>
    </div>
  </section>

  <section class="card card-front" aria-label="Business card, logo side">
    <div class="top-strip"></div>
    <div class="brand-name"><span class="brand-mark"></span>Maple Ridge Ventures</div>
    <div class="bottom-strip"></div>
  </section>

</body>
</html>
```